TEALCRATEMAN.COM NEEDS FACELIFT!!!

Please see www.tealcrateman.com for the basics. I am a glass artist who sells to retail market (art shows and e-commerce) as well as wholsale to art galleries nation wide. My site needs to serve both types of customer. I did the basics years ago, but now it's old and outdated . I need to totally rework the site, adding functionality as well as a new look.
My criteria are:
1. Need e-commerce page (cart) that allows for the rapid uploading of new artwork for my retail market.
2. Need separate login/e-commerce page for my wholesale customers as well as different pricing.
3. Need zip code lookup to show locations of current galleries.
4. Need registration page to collect customer emails/addresses for net marketing (constant contact).
5. Design should be neutral background since I want to highlight to vivid colors of my work.
6. Site should be easy to navigate.
7. I need to have control of adding content to site as needed (new photos, events, etc.)
8. Need page to list upcoming schedule and event dates.
9. Need all the pages and content from old site, with some revisions to be determined after general design is complete.
...Any suggestions on how to make my site more interesting and functional are welcomed!!
Added photos of newer work today, some of these should appear in high impact areas of the site,. DWight
Question to all...I just remembered that I have already search engine optimized my site using all the appropriate meta tags and photo names, text, etc. for the search terms "glass boxes" and "mosaic mirrors." I am number 1 in google search results of these terms. I need this to not change. Will redesigning my site affect this?
Reason: Hello all, I am in Rome italy right now on business and I have not had time to work with any of you on the designs yet. I am extending the deadline so I can provide more interaction . Dwight
Reason: I am still traveling abroad and have no time to work with and review designs. I will be home on the 26th of Oct. then I will be more in touch. Dwight
Target Market(s)
mid to high income women
Industry/Entity Type
E-Commerce
Requirements
Must have
- Separate shopping carts for retail and wholesale customers. Wholesale section requires login page.
Lots of pictures of my work. (will supply)
ZIP locator
Broken box repairs page. Customer describes broken piece and can buy replacement part. (size, color, knob color. Can provide pics of all the choices.)
Customer registration page to collect address and email for constant contact or direct mailing.
I like a black or dark gray background of some sort, unless you have a better idea to make my work stand out
Nice to have
- Some kind of link in to social media sites would be great!!!
Should not have
- keep the layout very simple and easy to navigate. Don't want a confusing page

```html
<!DOCTYPE html>
<html lang="en">
<head>
<meta charset="utf-8">
<title>Tealcrate Man – Glass Boxes, Mosaic Mirrors &amp; Tables</title>
<link href="https://fonts.googleapis.com/css2?family=Montserrat:wght@400;500;700&display=swap" rel="stylesheet">
<style>
:root{
  --header:#154c6b;
  --nav:#0e3a52;
  --logo:#8fc8e6;
  --ink:#1c1c1c;
  --muted:#333;
  --link:#1f4f8a;
  --panel:#efefef;
  --field:#e6e6e6;
  --mailfield:#6f8792;
  --footer:#103c55;
  --red:#d2281d;
  --white:#ffffff;
}
*{box-sizing:border-box;margin:0;padding:0}
html,body{width:873px;height:1200px;overflow:hidden}
body{
  position:relative;
  font-family:"Montserrat",Arial,sans-serif;
  color:var(--ink);
  background:linear-gradient(to bottom,var(--header) 0,#1d5878 140px,#6f9bb3 260px,#cfdfe8 360px,#ffffff 440px,#ffffff 100%);
}
.brand{position:absolute;left:62px;top:28px;font-size:31px;font-weight:700;letter-spacing:2px;color:var(--logo)}
.top-links{position:absolute;right:38px;top:44px;display:flex;gap:28px;font-size:11px;color:var(--white)}
.top-links a{display:flex;align-items:center;gap:8px;color:inherit;text-decoration:none;white-space:nowrap}
.top-links svg{width:20px;height:20px;fill:var(--white)}
.main-nav{position:absolute;left:28px;top:97px;width:812px;height:39px;background:var(--nav);border-radius:3px}
.main-nav a{position:absolute;top:0;line-height:39px;color:var(--white);text-decoration:none;font-size:10px;white-space:nowrap}
.hero-art{position:absolute;left:60px;top:176px;width:390px;height:290px;border-radius:6px;background:linear-gradient(135deg,#3d6b6f 0%,#1d3f86 25%,#b21f2a 50%,#c7b51e 75%,#86b93a 100%);opacity:.85}
.shop-now{position:absolute;left:441px;top:341px;width:79px;height:79px;border-radius:50%;background:radial-gradient(circle at 40% 30%,#5ec8ff,#0b74c2 70%);border:3px solid #e9f4fb;color:var(--white);font-weight:700;font-size:19px;line-height:22px;text-align:center;padding-top:15px;text-decoration:none}
.shop-now .cart{position:absolute;left:72px;top:48px;width:36px;height:30px}
.hero-copy{position:absolute;left:500px;top:225px;width:312px}
.hero-copy h2{font-weight:400;font-size:17px;margin-bottom:16px;padding-left:4px;white-space:nowrap}
.hero-copy p{margin-left:18px;font-size:12.6px;line-height:17.5px;color:var(--muted);text-align:center}
.welcome{position:absolute;left:33px;top:518px;width:535px}
.welcome h1{font-weight:400;font-size:18px;margin-bottom:16px}
.welcome p{font-size:10.2px;line-height:17.4px;padding-left:5px}
.panel-title{background:var(--panel);border-radius:3px;font-weight:400;font-size:14px;padding:0 12px;height:29px;line-height:29px}
.featured{position:absolute;left:39px;top:689px;width:531px}
.product-grid{position:absolute;left:41px;top:734px;display:grid;grid-template-columns:170px 170px 170px;column-gap:6px;row-gap:20px}
.product{text-align:center}
.product .shot{height:116px}
.product .shot.tower{background:linear-gradient(160deg,#1b2a44,#2f5f73 50%,#b8402a 80%,#1b2a44)}
.product .shot.stands{background:linear-gradient(160deg,#ffffff,#3a7bb3 45%,#d8c04a 70%,#9fcf5a)}
.product a{display:block;margin-top:7px;font-size:12px;color:var(--link);text-decoration:underline}
.sidebar{position:absolute;left:601px;top:530px;width:226px}
.events{list-style:none;margin-top:13px}
.events li{display:flex;gap:13px;align-items:flex-start;height:59px;padding-left:16px}
.events svg{width:42px;height:46px;flex:none}
.events p{font-size:8.6px;line-height:13px;margin-top:5px;color:var(--muted)}
.newsletter{margin-top:15px}
.newsletter p{font-size:8.6px;line-height:13px;padding:6px 10px 0 13px;color:var(--muted)}
.mail-field{display:block;margin:8px 0 0 23px;width:178px;height:19px;background:var(--mailfield);color:var(--white);font-size:10px;line-height:19px;padding-left:9px;border-radius:2px}
.text-link{display:block;text-align:center;font-size:10px;color:var(--muted);text-decoration:underline;margin-top:11px}
.register{margin-top:22px}
.register .row{display:flex;align-items:center;margin-top:9px;font-size:10px;padding-left:13px}
.register .row label{width:78px}
.register .row span{width:129px;height:20px;background:var(--field);border-radius:3px}
.register .row:first-of-type{margin-top:13px}
.register .text-link{margin-top:13px}
.site-footer{position:absolute;left:0;top:1080px;width:873px;height:120px;background:var(--footer);color:var(--white)}
.copyright{position:absolute;left:44px;top:29px;font-size:10.5px}
.legal{position:absolute;left:44px;top:53px;font-size:10.5px}
.legal a{color:inherit;text-decoration:none}
.social{position:absolute;left:48px;top:83px;display:flex;gap:6px}
.social span{width:19px;height:19px;border-radius:3px}
.shop-card{position:absolute;left:581px;top:23px;width:244px;height:72px;border-radius:3px;background:linear-gradient(to bottom,#ffffff,#dcdcdc)}
.shop-card .bags{position:absolute;left:6px;top:8px;width:78px;height:62px;background:linear-gradient(135deg,#f05a2a,#c4140f);border-radius:4px}
.shop-card h3{position:absolute;right:12px;top:10px;font-weight:400;font-size:17px;color:var(--ink)}
.shop-card a{position:absolute;right:13px;top:42px;font-size:13px;color:var(--red);text-decoration:none}
</style>
</head>
<body>

<header>
  <div class="brand">TEALCRATE MAN</div>
  <nav class="top-links">
    <a href="#"><svg viewBox="0 0 20 20"><path d="M2 8h16v11H2z M3 3h14l1 4H2z"/><rect x="8" y="12" width="4" height="7" fill="#154c6b"/></svg>Store Locator</a>
    <a href="#"><svg viewBox="0 0 20 20"><path d="M1 7c3-4 15-4 18 0l-1 2-4-1V6H6v2L2 9z"/><path d="M5 10h10l3 6H2z"/><circle cx="10" cy="13" r="2" fill="#154c6b"/></svg>Contact Us</a>
    <a href="#"><svg viewBox="0 0 20 20"><path d="M1 3h3l3 10h10l2-7H6l-.6-2H1z"/><circle cx="8" cy="17" r="1.6"/><circle cx="16" cy="17" r="1.6"/></svg>Shopping Cart</a>
  </nav>
  <nav class="main-nav">
    <a href="#" style="left:21px">Home</a>
    <a href="#" style="left:77px">About the Artist</a>
    <a href="#" style="left:172px">Glass Boxes</a>
    <a href="#" style="left:258px">Mosaic Mirrors</a>
    <a href="#" style="left:351px">Mosaic Tables</a>
    <a href="#" style="left:443px">Other Photos</a>
    <a href="#" style="left:533px">Store Locator</a>
    <a href="#" style="left:620px">Shop Online</a>
    <a href="#" style="left:705px">Show Schedule</a>
  </nav>
</header>

<section class="hero">
  <div class="hero-art" role="img" aria-label="Multi-drawer glass chest with colourful patterned drawers and glossy round knobs"></div>
  <div class="hero-copy">
    <h2>Sed do eiusmod tempor incididunt</h2>
    <p>Welcome to Dwight Halvorsen studio, home of TealCrateMan. This site features the creative works of Michigan artists Dwight Halvorsen and Ruth Pellman. Please browse through. We hope you enjoy our fun, whimsical and even elegant glass boxes, mirrors and contemporary sculpture.</p>
  </div>
  <a class="shop-now" href="#">SHOP<br>NOW
    <svg class="cart" viewBox="0 0 36 30"><path d="M2 4h5l4 14h18l4-11H9" fill="none" stroke="#9aa5ab" stroke-width="2"/><circle cx="14" cy="25" r="2.5" fill="#9aa5ab"/><circle cx="27" cy="25" r="2.5" fill="#9aa5ab"/></svg>
  </a>
</section>

<main>
  <section class="welcome">
    <h1>Welcome to Tealcrate Man</h1>
    <p>Welcome to Dwight Halvorsen studio, home of TealCrateMan. This site features the creative works of Michigan artists Dwight Halvorsen and Ruth Pellman. Please browse through. We hope you enjoy our fun, whimsical and even elegant glass boxes, mirrors and contemporary sculpture.Welcome to Dwight Halvorsen studio, home of TealCrateMan. This site features the creative works of Michigan artists Dwight Halvorsen and Ruth Pellman. Please browse through. We hope you enjoy our fun, whimsical and even elegant glass boxes, mirrors and contemporary sculpture.</p>
  </section>

  <section>
    <h2 class="panel-title featured">Featured Products</h2>
    <div class="product-grid">
      <div class="product"><div class="shot stands" role="img" aria-label="Patterned glass boxes on legs, hot item"></div><a href="#">Click for Glass Boxes</a></div>
      <div class="product"><div class="shot tower" role="img" aria-label="Stacked teal glass box tower"></div><a href="#">Click for Glass Boxes</a></div>
      <div class="product"><div class="shot tower" role="img" aria-label="Stacked teal glass box tower"></div><a href="#">Click for Glass Boxes</a></div>
      <div class="product"><div class="shot stands" role="img" aria-label="Patterned glass boxes on legs, hot item"></div><a href="#">Click for Glass Boxes</a></div>
      <div class="product"><div class="shot tower" role="img" aria-label="Stacked teal glass box tower"></div><a href="#">Click for Glass Boxes</a></div>
      <div class="product"><div class="shot tower" role="img" aria-label="Stacked teal glass box tower on sale"></div><a href="#">Click for Glass Boxes</a></div>
    </div>
  </section>
</main>

<aside class="sidebar">
  <h2 class="panel-title">Upcoming Events</h2>
  <ul class="events">
    <li><svg viewBox="0 0 42 46"><rect x="1" y="4" width="40" height="41" rx="3" fill="#fff" stroke="#333" stroke-width="2"/><rect x="2" y="5" width="38" height="11" fill="#2a84c6"/><text x="5" y="14" font-size="7" fill="#fff" font-family="Arial">SEP</text><text x="8" y="40" font-size="22" font-weight="700" fill="#222" font-family="Arial">12</text><rect x="9" y="1" width="3" height="7" fill="#333"/><rect x="30" y="1" width="3" height="7" fill="#333"/></svg><p>Lorem ipsum dolor sit amet, consectetur adipisicing elit, sed do eiusmod tempor ....</p></li>
    <li><svg viewBox="0 0 42 46"><rect x="1" y="4" width="40" height="41" rx="3" fill="#fff" stroke="#333" stroke-width="2"/><rect x="2" y="5" width="38" height="11" fill="#2a84c6"/><text x="5" y="14" font-size="7" fill="#fff" font-family="Arial">SEP</text><text x="8" y="40" font-size="22" font-weight="700" fill="#222" font-family="Arial">12</text><rect x="9" y="1" width="3" height="7" fill="#333"/><rect x="30" y="1" width="3" height="7" fill="#333"/></svg><p>Lorem ipsum dolor sit amet, consectetur adipisicing elit, sed do eiusmod tempor ....</p></li>
    <li><svg viewBox="0 0 42 46"><rect x="1" y="4" width="40" height="41" rx="3" fill="#fff" stroke="#333" stroke-width="2"/><rect x="2" y="5" width="38" height="11" fill="#2a84c6"/><text x="5" y="14" font-size="7" fill="#fff" font-family="Arial">SEP</text><text x="8" y="40" font-size="22" font-weight="700" fill="#222" font-family="Arial">12</text><rect x="9" y="1" width="3" height="7" fill="#333"/><rect x="30" y="1" width="3" height="7" fill="#333"/></svg><p>Lorem ipsum dolor sit amet, consectetur adipisicing elit, sed do eiusmod tempor ....</p></li>
  </ul>

  <section class="newsletter">
    <h2 class="panel-title">Newsletter</h2>
    <p>Lorem ipsum dolor sit amet, consectetur adipis icing elit, sed do eiusmod tempor ....</p>
    <span class="mail-field">Enter Mail ID</span>
    <a class="text-link" href="#">SUBSCRIBE</a>
  </section>

  <section class="register">
    <h2 class="panel-title">Quick User Registration</h2>
    <div class="row"><label>User Name :</label><span></span></div>
    <div class="row"><label>Password &nbsp;:</label><span></span></div>
    <a class="text-link" href="#">SIGN UP</a>
  </section>
</aside>

<footer class="site-footer">
  <p class="copyright">All Copyrights Reserved &nbsp;@ Tealcrate Man.com</p>
  <p class="legal"><a href="#">Terms and Conditions</a> | &nbsp;<a href="#">Privacy Policy</a> &nbsp;| &nbsp;<a href="#">Sitemap</a></p>
  <div class="social">
    <span style="background:#3b5a9a"></span>
    <span style="background:#3aa7dc"></span>
    <span style="background:#1d73ad"></span>
    <span style="background:#e8751a"></span>
  </div>
  <div class="shop-card">
    <div class="bags" role="img" aria-label="Red shopping bags"></div>
    <h3>Online Shopping</h3>
    <a href="#">Click Here</a>
  </div>
</footer>

</body>
</html>
```